Lark Ridge Property Biz Card
Business card and stationary
Project: Lark Ridge Property Biz Card
Lark Ridge Property Biz Card - Real Estate
Creative Brief
Professional
Dwight Fenmore
DO NOT ADD AN ADDRESS
dfenmore@larkridgeproperty.com
On the front I would like the logo, my name, phone number and email address. Also please have the catch phrase: "We buy houses, any condition! Get Cash Fast! Quick Closing!" The colour scheme of my logo is not set in stone, so please feel free to experiment with the colours.
On the back of the card please have the company logo

```html
<!DOCTYPE html>
<html lang="en">
<head>
<meta charset="utf-8">
<title>Lark Ridge Property – Stationery</title>
<link rel="stylesheet" href="https://fonts.googleapis.com/css2?family=Montserrat:wght@400;600;700&display=swap">
<style>
  :root{
    --navy:#1f3a6e;
    --navy-dark:#16294f;
    --ink:#1b1b1b;
    --grey:#6d7178;
    --rule:#c9ccd2;
    --paper:#ffffff;
    --backdrop:#e7e8ea;
  }
  *{box-sizing:border-box;margin:0;padding:0}
  html,body{width:1200px;height:857px;overflow:hidden}
  body{background:var(--backdrop);font-family:"Montserrat",Arial,sans-serif;color:var(--ink);position:relative}
  .sheet{position:absolute;background:var(--paper);box-shadow:0 2px 8px rgba(0,0,0,.12);overflow:hidden}
  .swoosh{position:absolute;display:block}
  .brand{display:flex;align-items:center;gap:7px;color:var(--navy);font-weight:700;letter-spacing:.02em;text-transform:uppercase}
  .brand-mark{background:var(--navy);flex:none}
  .brand--light{color:#fff}
  .brand--light .brand-mark{background:#fff}

  /* Letterhead */
  .letterhead{left:40px;top:40px;width:340px;height:480px;padding:28px 30px}
  .letterhead .brand{font-size:13px}
  .letterhead .brand-mark{width:14px;height:14px}
  .letter-contact{position:absolute;right:30px;top:30px;text-align:right;font-size:7px;line-height:1.6;color:var(--grey)}
  .letter-body{margin-top:48px;font-size:7.2px;line-height:1.65;color:#333;max-width:250px}
  .letter-body p{margin-bottom:9px}
  .letter-sign{margin-top:22px;font-size:7.2px;line-height:1.6}
  .letter-sign strong{color:var(--navy)}
  .letterhead .swoosh{left:0;bottom:0;width:340px;height:90px}

  /* Fax sheet */
  .fax{left:410px;top:40px;width:340px;height:480px;padding:28px 30px}
  .fax .brand{font-size:13px}
  .fax .brand-mark{width:14px;height:14px}
  .fax-title{position:absolute;right:30px;top:26px;font-size:22px;font-weight:600;letter-spacing:.25em;color:var(--grey)}
  .fax-fields{margin-top:40px;width:100%;border-collapse:collapse;font-size:8px}
  .fax-fields th{width:56px;text-align:left;font-weight:600;color:var(--navy);padding:7px 0}
  .fax-fields td{border-bottom:1px solid var(--rule)}
  .fax-checks{display:flex;gap:14px;margin-top:20px;font-size:7.5px;color:var(--grey)}
  .fax-checks span{display:flex;align-items:center;gap:4px}
  .fax-checks i{width:8px;height:8px;border:1px solid var(--grey);display:block}
  .fax-comments{margin-top:20px;font-size:8px;font-weight:600;color:var(--navy)}
  .fax-lines{margin-top:6px}
  .fax-lines div{height:18px;border-bottom:1px solid var(--rule)}
  .fax-foot{position:absolute;left:30px;bottom:22px;font-size:7px;color:var(--grey)}
  .fax .swoosh{right:0;top:0;width:120px;height:480px}

  /* Business cards */
  .card{width:350px;height:200px}
  .card-front{left:800px;top:40px;padding:22px 24px}
  .card-front .brand{font-size:12px}
  .card-front .brand-mark{width:13px;height:13px}
  .card-name{margin-top:26px;font-size:15px;font-weight:700;color:var(--navy)}
  .card-title{font-size:8px;color:var(--grey);margin-top:2px;letter-spacing:.05em}
  .card-contact{margin-top:12px;font-size:8.5px;line-height:1.7}
  .card-tagline{position:absolute;left:24px;bottom:14px;width:220px;font-size:7.5px;font-weight:600;color:var(--navy);line-height:1.4}
  .card-front .swoosh{right:0;top:0;width:110px;height:200px}

  .card-back{left:800px;top:265px;background:var(--navy);display:flex;align-items:center;justify-content:center}
  .card-back .brand{font-size:16px;position:relative;z-index:1}
  .card-back .brand-mark{width:16px;height:16px}
  .card-back .swoosh{left:0;top:0;width:350px;height:200px}

  /* Envelope */
  .envelope{left:800px;top:490px;width:350px;height:175px;padding:18px 20px}
  .envelope .brand{font-size:11px}
  .envelope .brand-mark{width:12px;height:12px}
  .envelope-return{font-size:7px;color:var(--grey);margin-top:5px;margin-left:19px}
  .envelope .swoosh{left:0;bottom:0;width:350px;height:60px}

  /* Compliment slip */
  .slip{left:40px;top:555px;width:710px;height:250px;padding:28px 34px}
  .slip .brand{font-size:15px}
  .slip .brand-mark{width:16px;height:16px}
  .slip-note{margin-top:22px;font-size:12px;color:var(--grey);font-weight:600;letter-spacing:.08em}
  .slip-contact{position:absolute;left:34px;bottom:26px;font-size:8px;color:var(--grey);line-height:1.6}
  .slip .swoosh{right:0;top:0;width:240px;height:250px}
</style>
</head>
<body>

<section class="sheet letterhead">
  <div class="brand"><span class="brand-mark"></span>Lark Ridge Property</div>
  <div class="letter-contact">(204) 555-0148<br>dfenmore@larkridgeproperty.com</div>
  <div class="letter-body">
    <p>Dear Homeowner,</p>
    <p>Thank you for contacting us about your home. We buy houses in any condition and can offer a fair cash price within days.</p>
    <p>Our team handles every step, from the first visit to a quick closing, so you never pay fees or repairs.</p>
    <p>Please call me directly to arrange a free, no obligation review of your property.</p>
  </div>
  <div class="letter-sign">Sincerely,<br><br><strong>Dwight Fenmore</strong><br>Property Consultant</div>
  <svg class="swoosh" viewBox="0 0 340 90" preserveAspectRatio="none" aria-hidden="true">
    <path d="M0,90 L0,30 C120,80 240,80 340,40 L340,90 Z" fill="var(--navy)"/>
    <path d="M0,30 C120,80 240,80 340,40 L340,30 C240,68 120,68 0,22 Z" fill="var(--ink)"/>
  </svg>
</section>

<section class="sheet fax">
  <div class="brand"><span class="brand-mark"></span>Lark Ridge Property</div>
  <div class="fax-title">FAX</div>
  <table class="fax-fields">
    <tr><th>To</th><td></td></tr>
    <tr><th>From</th><td></td></tr>
    <tr><th>Fax</th><td></td></tr>
    <tr><th>Phone</th><td></td></tr>
    <tr><th>Date</th><td></td></tr>
    <tr><th>Pages</th><td></td></tr>
    <tr><th>Re</th><td></td></tr>
  </table>
  <div class="fax-checks">
    <span><i></i>Urgent</span><span><i></i>For Review</span><span><i></i>Please Reply</span><span><i></i>Please Comment</span>
  </div>
  <div class="fax-comments">Comments:</div>
  <div class="fax-lines"><div></div><div></div><div></div><div></div><div></div></div>
  <div class="fax-foot">(204) 555-0148 · dfenmore@larkridgeproperty.com</div>
  <svg class="swoosh" viewBox="0 0 120 480" preserveAspectRatio="none" aria-hidden="true">
    <path d="M120,0 L90,0 C115,70 118,120 120,150 Z" fill="var(--navy)"/>
  </svg>
</section>

<section class="sheet card card-front">
  <div class="brand"><span class="brand-mark"></span>Lark Ridge Property</div>
  <div class="card-name">Dwight Fenmore</div>
  <div class="card-title">Property Consultant</div>
  <div class="card-contact">(204) 555-0148<br>dfenmore@larkridgeproperty.com</div>
  <div class="card-tagline">We buy houses, any condition! Get Cash Fast! Quick Closing!</div>
  <svg class="swoosh" viewBox="0 0 110 200" preserveAspectRatio="none" aria-hidden="true">
    <path d="M110,0 L60,0 C30,70 40,140 110,200 Z" fill="var(--navy)"/>
    <path d="M60,0 C30,70 40,140 110,200 L100,200 C30,140 22,70 50,0 Z" fill="var(--ink)"/>
  </svg>
</section>

<section class="sheet card card-back">
  <svg class="swoosh" viewBox="0 0 350 200" preserveAspectRatio="none" aria-hidden="true">
    <path d="M0,0 L140,0 C90,70 60,140 0,200 Z" fill="var(--ink)"/>
    <path d="M140,0 C90,70 60,140 0,200 L0,188 C52,135 82,70 128,0 Z" fill="var(--navy-dark)"/>
  </svg>
  <div class="brand brand--light"><span class="brand-mark"></span>Lark Ridge Property</div>
</section>

<section class="sheet envelope">
  <div class="brand"><span class="brand-mark"></span>Lark Ridge Property</div>
  <div class="envelope-return">(204) 555-0148 · larkridgeproperty.com</div>
  <svg class="swoosh" viewBox="0 0 350 60" preserveAspectRatio="none" aria-hidden="true">
    <path d="M0,60 L0,20 C110,55 240,55 350,10 L350,60 Z" fill="var(--navy)"/>
    <path d="M0,20 C110,55 240,55 350,10 L350,2 C240,46 110,46 0,12 Z" fill="var(--ink)"/>
  </svg>
</section>

<section class="sheet slip">
  <div class="brand"><span class="brand-mark"></span>Lark Ridge Property</div>
  <div class="slip-note">WITH COMPLIMENTS</div>
  <div class="slip-contact">Dwight Fenmore · (204) 555-0148<br>dfenmore@larkridgeproperty.com</div>
  <svg class="swoosh" viewBox="0 0 240 250" preserveAspectRatio="none" aria-hidden="true">
    <path d="M240,0 L120,0 C70,90 110,190 240,250 Z" fill="var(--navy)"/>
    <path d="M120,0 C70,90 110,190 240,250 L222,250 C96,190 56,90 104,0 Z" fill="var(--ink)"/>
  </svg>
</section>

</body>
</html>
```